Business that Cleans the dishes and utensils used in private jets needs a flyer to describe its b...

I need a flyer to describe a HK based company called 'Vantor Rinsing'. We help the flight attendants to clean valuable dishes and utensils to save them time and costs. Color green is preferable. The design shall be easy to read and clear

Target Market(s)

Flight attendants and flight operations management

Industry/Entity Type

Aviation

Colors

Designer to choose colors to be used in the design.

Requirements
Must have
• Clean and professional.

```html
<!DOCTYPE html>
<html lang="en">
<head>
<meta charset="utf-8">
<title>Vantor Rinsing – Flyer</title>
<link href="https://fonts.googleapis.com/css2?family=Montserrat:wght@400;500;700;800&display=swap" rel="stylesheet">
<style>
  :root {
    --green: #6fcf17;
    --yellow: #f0b323;
    --white: #ffffff;
    --ink: #111111;
    --sky-top: #8fb9df;
    --sky-mid: #d9dee6;
    --ground: #a99580;
    --pale: #eef1f3;
  }
  * { margin: 0; padding: 0; box-sizing: border-box; }
  html, body { width: 927px; height: 1200px; overflow: hidden; background: var(--white); }
  body { font-family: 'Montserrat', sans-serif; }
  .flyer { position: relative; width: 927px; height: 1200px; overflow: hidden; background: var(--white); }
  .backdrop { position: absolute; inset: 0; }
  .brand { position: absolute; left: 62px; top: 70px; display: flex; align-items: center; gap: 12px; }
  .brand-dot { width: 44px; height: 44px; border-radius: 50%; background: var(--green); }
  .brand-name { font-weight: 700; font-size: 26px; color: var(--green); line-height: 1.05; width: 150px; }
  .title { position: absolute; left: 465px; top: 68px; width: 380px; text-align: center; }
  .title-main { font-weight: 800; font-size: 82px; color: var(--white); letter-spacing: 1px; line-height: 1; white-space: nowrap; }
  .title-sub { font-weight: 700; font-size: 56px; color: var(--yellow); letter-spacing: 1px; line-height: 1.15; white-space: nowrap; }
  .feature { position: absolute; left: 212px; top: 604px; width: 320px; color: var(--white); text-align: center; }
  .feature h2 { font-weight: 700; font-size: 30px; line-height: 1.1; margin-bottom: 10px; }
  .feature p { font-weight: 500; font-size: 17px; line-height: 1.3; }
  .side-note { position: absolute; left: 90px; top: 790px; width: 250px; color: var(--white); font-size: 8.8px; line-height: 1.5; text-align: justify; }
  .about { position: absolute; left: 432px; top: 734px; width: 438px; }
  .about h2 { font-weight: 700; font-size: 34px; color: var(--ink); text-align: right; margin-bottom: 12px; }
  .about p { font-size: 18.2px; line-height: 1.22; color: var(--ink); text-align: justify; }
  .contact { position: absolute; left: 73px; top: 1062px; }
  .contact h3 { font-weight: 700; font-size: 17px; color: var(--yellow); margin-bottom: 8px; }
  .contact p { font-size: 19px; color: var(--ink); line-height: 1.4; }
  .web { position: absolute; right: 82px; top: 1118px; font-size: 26px; font-weight: 500; color: var(--ink); }
  .web b { color: var(--green); font-weight: 700; }
</style>
</head>
<body>
<main class="flyer">
  <svg class="backdrop" width="927" height="1200" viewBox="0 0 927 1200">
    <defs>
      <linearGradient id="jetScene" x1="0" y1="0" x2="0" y2="1">
        <stop offset="0" stop-color="var(--sky-top)"/>
        <stop offset="0.5" stop-color="var(--sky-mid)"/>
        <stop offset="0.62" stop-color="#c6c0b6"/>
        <stop offset="1" stop-color="var(--ground)"/>
      </linearGradient>
      <linearGradient id="washScene" x1="0" y1="0" x2="1" y2="1">
        <stop offset="0" stop-color="#c9d6de"/>
        <stop offset="1" stop-color="#f3f5f6"/>
      </linearGradient>
      <linearGradient id="cabinScene" x1="0" y1="0" x2="0" y2="1">
        <stop offset="0" stop-color="#e6e3dc"/>
        <stop offset="0.6" stop-color="#8d8780"/>
        <stop offset="1" stop-color="#2d2b29"/>
      </linearGradient>
    </defs>
    <rect class="photo-jet" x="0" y="0" width="927" height="760" fill="url(#jetScene)" role="img" aria-label="Photo of a private jet parked on the apron with its stairs down"/>
    <path class="corner-edge" d="M0,0 L500,0 C410,70 355,220 215,290 C140,326 60,318 0,306 Z" fill="var(--yellow)"/>
    <path class="corner-panel" d="M0,0 L478,0 C392,62 340,205 200,272 C130,305 60,300 0,290 Z" fill="var(--white)"/>
    <path class="wave-green" d="M180,620 C260,545 400,560 520,520 L927,430 L927,640 C760,640 620,660 540,710 C460,750 330,748 200,748 C170,720 160,660 180,620 Z" fill="var(--green)"/>
    <path class="lower-base" d="M0,712 C150,740 330,752 460,740 C600,690 780,645 927,640 L927,1200 L0,1200 Z" fill="var(--white)"/>
    <path class="wave-yellow" d="M0,712 C200,700 400,712 455,762 C478,805 425,880 335,940 C245,1000 120,1030 0,1042 Z" fill="var(--yellow)"/>
    <path class="text-panel" d="M462,742 C385,800 405,900 335,980 C275,1050 200,1120 120,1200 L927,1200 L927,645 C780,655 600,685 462,742 Z" fill="var(--white)"/>
    <path class="lower-shade" d="M0,1060 C80,1100 150,1150 180,1200 L0,1200 Z" fill="var(--pale)"/>
    <path class="corner-swoosh" d="M927,950 C905,1075 855,1160 770,1200 L927,1200 Z" fill="var(--green)"/>
    <circle class="photo-wash" cx="626" cy="528" r="120" fill="url(#washScene)" stroke="var(--white)" stroke-width="6" role="img" aria-label="Photo of gloved hands washing a dish in water"/>
    <circle class="photo-cabin" cx="822" cy="482" r="150" fill="url(#cabinScene)" stroke="var(--white)" stroke-width="6" role="img" aria-label="Photo of a set dining table in a private jet cabin"/>
  </svg>

  <div class="brand">
    <span class="brand-dot"></span>
    <span class="brand-name">Vantor Rinsing</span>
  </div>

  <div class="title">
    <div class="title-main">VANTOR</div>
    <div class="title-sub">RINSING</div>
  </div>

  <section class="feature">
    <h2>LOREM IPSUM</h2>
    <p>Lorem Ipsum is simply dummy text of the printing and typesetting industry.</p>
  </section>

  <p class="side-note">Lorem Ipsum is simply dummy text of the printing and typesetting industry. Lorem Ipsum has been the industry's standard dummy text ever since the 1500s, when an unknown printer took a galley of type and scrambled it to make a type specimen book. Lorem Ipsum is simply dummy text of the printing and typesetting industry.</p>

  <section class="about">
    <h2>LOREM IPSUM</h2>
    <p>Lorem Ipsum is simply dummy text of the printing and typesetting industry. Lorem Ipsum has been the industry's standard dummy text ever since the 1500s, when an unknown printer took a galley of type and scrambled it to make a type specimen book. Lorem Ipsum is simply dummy text of the printing and typesetting industry. Lorem Ipsum has been the industry's standard dummy text ever since the 1500s, when an unknown printer took a galley of type</p>
  </section>

  <section class="contact">
    <h3>CONTACT US :</h3>
    <p>0900 412 3388</p>
    <p>hello@vantorrinsing.com</p>
  </section>

  <p class="web">www.<b>VANTORRINSING</b>.com</p>
</main>
</body>
</html>
```